Visitenkarten-Design Neutrale Verzollungs Agentur für den Grenzverkehr des Zollwesens
Sehr schnelle Umsetzung nach unserer Vorstellung,und sehr netter und guter Umgang in der Kominikation. tolvix hat unsere erwartung zu 100 % übertroffen.
Zielgruppe
Wir sind eine Neutrale Verzollungs Agentur für den Grenzverkehr des Zollwesens
Bluefield & Meridian Group
Wir führen für Kunden die Zollabwicklungen ab.
Seefracht - Bahnfracht-Luftfracht-LKW Fracht
Cargo - Hersteller Firmen und Endknden International
Aufgabenstellung
Rückseite sollte mitgestaltet werden

```html
<!DOCTYPE html>
<html lang="de">
<head>
<meta charset="utf-8">
<title>Grenzlicht – Visitenkarte</title>
<link rel="stylesheet" href="https://fonts.googleapis.com/css2?family=Exo+2:wght@600&family=Open+Sans:wght@600&family=Questrial&display=swap">
<style>
  :root {
    --backdrop: #c8c8c8;
    --paper: #ffffff;
    --ink-grey: #4f4f4f;
    --ink-dark: #3c3c3c;
    --accent-blue: #4a8ccd;
    --stripe: #ebecf3;
    --divider: #9fb8cc;
    --band-start: #3a87a6;
    --band-end: #154a7d;
    --back-start: #3683a5;
    --back-end: #0b386f;
    --logo-light: #c9dbef;
  }
  * { margin: 0; padding: 0; box-sizing: border-box; }
  html, body { width: 1073px; height: 1200px; overflow: hidden; background: var(--backdrop); }
  .canvas { position: relative; width: 1073px; height: 1200px; }

  .card { position: absolute; overflow: hidden; }
  .card--front {
    left: 139px; top: 141px; width: 793px; height: 457px;
    background: var(--paper);
    box-shadow: 1px 1px 3px rgba(0,0,0,.35);
  }
  .card--back {
    left: 144px; top: 658px; width: 787px; height: 456px;
    background: linear-gradient(90deg, var(--back-start) 0%, #2a6f9a 45%, var(--back-end) 100%);
  }

  .stripes { position: absolute; left: 0; top: 35px; width: 100%; height: 104px; }
  .stripes span { position: absolute; left: 0; width: 100%; height: 2px; background: var(--stripe); }

  .brand-plate {
    position: absolute; left: 92px; top: 70px; width: 238px; height: 100px;
    background: var(--paper); border-radius: 50px;
  }
  .brand-name {
    position: absolute; font-family: "Exo 2", sans-serif; font-weight: 600; white-space: nowrap;
  }
  .card--front .brand-name { left: 104px; top: 100px; font-size: 36px; color: var(--ink-dark); }
  .brand-dot { position: absolute; border-radius: 50%; }
  .card--front .brand-dot { left: 300px; top: 117px; width: 14px; height: 14px; background: var(--accent-blue); }

  .countries {
    position: absolute; left: 391px; top: 125px;
    font-family: "Open Sans", sans-serif; font-weight: 600; font-size: 14px; color: var(--ink-grey);
  }

  .company {
    position: absolute; right: 470px; top: 232px; text-align: right;
    font-family: "Exo 2", sans-serif; font-weight: 600; font-size: 20px; line-height: 25px; color: var(--accent-blue);
  }
  .address {
    position: absolute; right: 470px; top: 314px; text-align: right;
    font-family: "Questrial", sans-serif; font-size: 20px; line-height: 24px; color: var(--ink-grey);
  }
  .divider { position: absolute; left: 381px; top: 229px; width: 1px; height: 164px; background: var(--divider); }
  .contact {
    position: absolute; left: 448px; font-family: "Questrial", sans-serif;
    font-size: 20px; line-height: 25px; color: var(--ink-grey);
  }
  .contact--phone { top: 244px; }
  .contact--web { top: 318px; }
  .footer-band {
    position: absolute; left: 2px; right: 0; bottom: 0; height: 22px;
    background: linear-gradient(90deg, var(--band-start) 0%, #2c7399 50%, var(--band-end) 100%);
  }

  .globe {
    position: absolute; left: 39px; top: -27px; width: 522px; height: 522px; border-radius: 50%;
    background: radial-gradient(circle at 42% 52%, #d9e6f5 0%, #a9c4e6 28%, #5f9bb4 48%, rgba(60,130,165,.6) 70%, rgba(60,130,165,0) 100%);
    border: 1px solid rgba(255,255,255,.35);
  }
  .card--back .brand-name { left: 446px; top: 180px; font-size: 46px; color: var(--logo-light); }
  .card--back .brand-dot { left: 712px; top: 201px; width: 16px; height: 16px; background: var(--logo-light); }
</style>
</head>
<body>
<main class="canvas">
  <section class="card card--front" aria-label="Vorderseite">
    <div class="stripes" aria-hidden="true">
      <span style="top:0"></span><span style="top:10px"></span><span style="top:20px"></span>
      <span style="top:33px"></span><span style="top:48px"></span><span style="top:58px"></span>
      <span style="top:70px"></span><span style="top:82px"></span><span style="top:94px"></span>
      <span style="top:102px"></span>
    </div>
    <div class="brand-plate" aria-hidden="true"></div>
    <div class="brand-name">Grenzlicht</div>
    <div class="brand-dot" aria-hidden="true"></div>
    <p class="countries">Switzerland · Germany · Denmark · France</p>

    <p class="company">Bluefield &amp; Meridian<br>Group GmbH</p>
    <p class="address">Lindenweg 52<br>A-3910 Marbach</p>
    <div class="divider" aria-hidden="true"></div>
    <p class="contact contact--phone">Tel: 04411/728 39-21<br>Fax: 04411/728 39-31</p>
    <p class="contact contact--web">E-mail: service@grenzlicht-zoll.com<br>Web: www.grenzlicht-zoll.com</p>
    <div class="footer-band" aria-hidden="true"></div>
  </section>

  <section class="card card--back" aria-label="Rückseite">
    <div class="globe" role="img" aria-label="Globus mit Längen- und Breitengraden und den Kontinenten Nord- und Südamerika"></div>
    <div class="brand-name">Grenzlicht</div>
    <div class="brand-dot" aria-hidden="true"></div>
  </section>
</main>
</body>
</html>
```